K.O.V Ventures - Business Card

We need a business card design for a new company based in Malaysia, called K.O.V Ventures Sdn. Bhd. We create, develop & customize database & software/web-based business systems to suit our clients need, mainly in oil&gas industry.

We would like to challenge the creativity of you to design a simple, meaningful, modern, professional & sleek. The design concept may varies but worthy enough for the recipients to proudly keep it in their wallet, and award us with fruitful business opportunities.

B-7-12 Lantera Plaza,
PJU9/4, Damai Perdana,
47500 Selangor. Malaysia

http://kovventures-example.com

HAFIZ Rosman | +6012-7038812 | Co-Founder
Di Kamarul | +6012-4190273 | Co-Founder
Amir Syukri | +6019-3306158 | Managing Director

Target Market(s)

The target market will expand to several other industries such as aviation, communication, automotive, education & hotel.

Industry/Entity Type

Business

Font styles to use
Serif
Sans Serif
Decorative
Script

Requirements
Must have
• plain background yet colourful concept.
Should not have
• something too easy that I can draw myself

```html
<!DOCTYPE html>
<html lang="en">
<head>
<meta charset="utf-8">
<title>K.O.V Ventures - Business Card</title>
<link rel="stylesheet" href="https://fonts.googleapis.com/css2?family=Arimo:wght@400;700&display=swap">
<style>
  :root {
    --backdrop: #2b2b2b;
    --card: #f4f4f2;
    --ink: #1c1c1c;
    --ink-soft: #2e2e2e;
    --pink: #d6567f;
    --purple: #6a4f8e;
    --green: #5f9a55;
    --orange: #d9924a;
    --magenta: #a84c86;
  }
  * { box-sizing: border-box; margin: 0; padding: 0; }
  html, body {
    width: 1200px;
    height: 797px;
    overflow: hidden;
    background: var(--backdrop);
  }
  .stage {
    width: 1200px;
    height: 797px;
    display: flex;
    align-items: center;
    justify-content: center;
  }
  .business-card {
    position: relative;
    width: 700px;
    height: 400px;
    background: var(--card);
    box-shadow: 0 10px 30px rgba(0,0,0,0.45);
    font-family: "Arimo", Arial, sans-serif;
    color: var(--ink);
  }
  .brand {
    position: absolute;
    left: 70px;
    top: 44px;
    display: flex;
    align-items: center;
    gap: 12px;
  }
  .brand-dot {
    width: 34px;
    height: 34px;
    border-radius: 50%;
    background: var(--purple);
  }
  .brand-name {
    font-size: 22px;
    font-weight: 700;
    color: var(--purple);
    letter-spacing: 0.5px;
  }
  .contact {
    position: absolute;
    left: 70px;
    top: 118px;
  }
  .person-name {
    font-size: 28px;
    font-weight: 700;
    letter-spacing: 0.5px;
  }
  .person-role {
    font-size: 19px;
    margin-top: 4px;
    margin-bottom: 22px;
  }
  .details {
    list-style: none;
    font-size: 18px;
    line-height: 25px;
    color: var(--ink-soft);
  }
  .accent-dashes {
    display: flex;
    gap: 18px;
    margin-top: 14px;
  }
  .accent-dashes span {
    width: 12px;
    height: 6px;
    border-radius: 3px;
  }
  .colour-strip {
    position: absolute;
    left: 0;
    right: 0;
    bottom: 0;
    height: 26px;
    display: flex;
  }
  .colour-strip span { flex: 1; }
  .c-pink { background: var(--pink); }
  .c-purple { background: var(--purple); }
  .c-green { background: var(--green); }
  .c-orange { background: var(--orange); }
  .c-magenta { background: var(--magenta); }
</style>
</head>
<body>
  <main class="stage">
    <article class="business-card">
      <header class="brand">
        <span class="brand-dot"></span>
        <span class="brand-name">K.O.V Ventures</span>
      </header>
      <section class="contact">
        <h1 class="person-name">HAFIZ ROSMAN</h1>
        <p class="person-role">Co-Founder</p>
        <ul class="details">
          <li>B-7-12 Lantera Plaza,</li>
          <li>PJU9/4, Damai Perdana.</li>
          <li>46350 Kelana Jaya.Malaysia.</li>
          <li>+6012-7038812</li>
          <li>www.kovventures-example.com</li>
        </ul>
        <div class="accent-dashes">
          <span class="c-pink"></span>
          <span class="c-purple"></span>
          <span class="c-green"></span>
          <span class="c-orange"></span>
          <span class="c-magenta"></span>
        </div>
      </section>
      <footer class="colour-strip">
        <span class="c-pink"></span>
        <span class="c-purple"></span>
        <span class="c-green"></span>
        <span class="c-orange"></span>
        <span class="c-magenta"></span>
      </footer>
    </article>
  </main>
</body>
</html>
```